Community Legal Website

The website is about a law in legal area (Fiscal), it has a moderator and the community also contributes with information.

Attention that this is not for a Law Firm. This is a community site where all the lawyers can contribute wiith their knowledge and at the same time where they can read the Official Law in the fiscal area.

The site is in portuguese, but we have attach information in english about the functionalities.

I attach information which represents the first version of the site done by html.. That is the site we intend to improve.

The site is quite simple because the main pages are:
- Home page;
- Section page (which has the Chapters and articles)
- Article page;

This pages all belong to the article:

redaccao_actual.htm, redaccoes_anteriores.htm, anotacoes.htm, jurisprudencia.htm, decisoesadministrativas.htm, minutas.htm, duvidas.htm

AS you see in all of them the options are always there.

The most important in this site is the usability of the content:

The FAQ, Contacts, Terms of conditions, who we are, are links less important.

Also there is a possibility to have in the homepage a higligh of certain articles that we want to raise from the others.

Please check the excel sheet as well as the zip file wich has the site in portuguese that you can use a website translator to check in your language.
Updates

We added a excel sheet with the functionalities in english which the site must have.

Reason: Because this is easter time we have increased the time for the deliver

Please check briefing update.

Reason: There were some request to extend the deadline because of the Easter

Hi!

Please read carefully the briefing. People are presenting me company web sites adn this is NOT a company web site. THis is a Site wich has a content of Laws. Please check the 1st version in the zip file and improve it. The options are there and you can translate in google tradutor or reading the excel sheet attach.

txs,
KM

Reason: My client need more desing choices

Target Market(s)

Lawyers, jurists and people related with the fiscal Law.

Industry/Entity Type

Legal

Requirements
Must have
• The interface should be clean and elegant.
It should also contribute to speed.
And try to avoid to many distract elements.
The site will be dinamic and with a backoffice, so in that you have to be carefully with the space dynamic. But you don't have to worry about the backoffice. Only the front office which is the public site.

```html
<!DOCTYPE html>
<html lang="en">
<head>
<meta charset="utf-8">
<title>Lexa Fiscal – Home</title>
<link href="https://fonts.googleapis.com/css2?family=Arimo:wght@400;700&display=swap" rel="stylesheet">
<style>
:root{
  --red:#bf2a1c;
  --brown:#2b0f05;
  --ink:#222;
  --page:#ffffff;
  --backdrop:#e9e9e9;
  --row:#dedede;
  --panel:#f4f4f4;
  --footer-top:#3a3a3a;
  --footer-bottom:#0d0d0d;
}
*{box-sizing:border-box;margin:0;padding:0}
html,body{width:1014px;height:1200px;overflow:hidden}
body{background:var(--backdrop);font-family:"Arimo",Arial,sans-serif;color:var(--ink);position:relative}
.page{position:absolute;left:86px;top:0;width:846px;height:1200px;background:var(--page);box-shadow:0 0 12px rgba(0,0,0,.25)}

.brand{position:absolute;left:18px;top:34px}
.brand-name{font-size:30px;font-weight:400;color:var(--brown);letter-spacing:1px}

.utility{position:absolute;left:451px;top:59px;font-size:11.5px;color:var(--brown);display:flex;gap:14px}
.search{position:absolute;left:647px;top:51px;width:186px;height:32px;border-radius:16px;background:linear-gradient(#e6e6e6,#f7f7f7);box-shadow:inset 0 1px 3px rgba(0,0,0,.3)}
.search svg{position:absolute;left:9px;top:8px}

.nav{position:absolute;left:0;top:107px;width:846px;height:39px;background:var(--brown);display:flex}
.nav a{color:#fff;text-decoration:none;font-size:13px;display:flex;align-items:center;justify-content:center;border-right:1px solid #4a2416}
.nav a.active{background:var(--red)}

.hero{position:absolute;left:0;top:146px;width:846px;height:361px;background:linear-gradient(180deg,#e9e9e9 0%,#d0d0d0 45%,#8f8a86 80%,#f2f2f2 100%)}
.hero-title{position:absolute;left:33px;top:71px;width:359px;height:106px;background:rgba(255,255,255,.45);padding:0 0 0 5px}
.hero-title .l1{font-size:52px;font-weight:700;color:var(--brown);line-height:52px;display:block}
.hero-title .l2{font-size:52px;color:var(--red);line-height:52px;display:block}
.hero svg{position:absolute;left:811px;top:120px}

.welcome{position:absolute;left:13px;top:524px;width:816px}
.welcome h1{font-size:22px;font-weight:400;color:var(--brown)}
.welcome h1 span{color:var(--red)}
.welcome p{margin-top:3px;font-size:11.4px;line-height:15.2px;text-align:justify;padding-left:2px}
.more{position:absolute;left:15px;top:131px;height:20px;display:flex;font-size:11px;color:#fff}
.more span{background:#3b3b3b;padding:3px 5px}
.more i{background:var(--red);width:12px;display:flex;align-items:center;justify-content:center;font-style:normal}

.law{position:absolute;left:15px;width:814px;background:var(--panel);border:1px solid #ddd;border-radius:5px}
.law h2{height:39px;background:var(--red);color:#fff;border-radius:5px;font-size:22px;font-weight:400;text-align:center;line-height:39px}
.law ul{list-style:none}
.law li{height:34px;background:var(--row);font-size:11.5px;line-height:34px;padding-left:12px;margin-bottom:14px}
.fiscal{top:698px;height:263px}
.fiscal ul{padding-top:29px}
.admin{top:993px;height:106px}
.admin ul{padding-top:17px}

.footer{position:absolute;left:0;top:1131px;width:846px;height:69px;background:linear-gradient(var(--footer-top),var(--footer-bottom));color:#fff}
.footer-links{position:absolute;left:14px;top:14px;font-size:10.5px;font-weight:700;display:flex;gap:11px}
.copyright{position:absolute;left:14px;top:34px;font-size:10.5px}
.follow{position:absolute;left:610px;top:21px;font-size:10px}
.social{position:absolute;left:666px;top:22px;display:flex;gap:6px}
.social span{width:24px;height:24px;display:block}
</style>
</head>
<body>
<div class="page">
  <header>
    <div class="brand"><span class="brand-name">Lexa Fiscal</span></div>
    <nav class="utility"><span>Sitemap</span><span>|</span><span>Support</span><span>|</span><span>Search</span></nav>
    <div class="search">
      <svg width="17" height="17" viewBox="0 0 17 17"><circle cx="6.5" cy="6.5" r="5" fill="none" stroke="#444" stroke-width="1.6"/><line x1="10" y1="10" x2="15.5" y2="15.5" stroke="#444" stroke-width="2.4"/></svg>
    </div>
  </header>
  <nav class="nav">
    <a class="active" style="width:96px">Home</a>
    <a style="width:102px">Services</a>
    <a style="width:117px">Resources</a>
    <a style="width:106px">Partners</a>
    <a style="width:90px">About</a>
    <a style="width:97px;border-right:0">Contacts</a>
  </nav>
  <section class="hero" role="img" aria-label="Group of smiling professionals in business suits in front of a faint world map">
    <div class="hero-title"><span class="l1">Ask</span><span class="l2">professionals!</span></div>
    <svg width="22" height="36" viewBox="0 0 22 36"><polyline points="2,2 19,18 2,34" fill="none" stroke="#2b0f05" stroke-width="2.5"/></svg>
  </section>
  <section class="welcome">
    <h1>Welcome to <span>our website...</span></h1>
    <p>simply dummy text of the printing and typesetting industry. Lorem Ipsum has been the industry's standard dummy text ever since the 1500s, when an unknown printer took a galley of type and scrambled it to make a type specimen book.simply dummy text of the printing and typesetting industry. Lorem Ipsum has been the industry's standard dummy text ever since the 1500s, when an unknown printer took a galley of type and scrambled it to make a type specimen book. It has survived not only five centuries, but also the leap into electronic typesetting, remaining essentially unchanged. It was popularised in the 1960s with the release of Typeline sheets containing Lorem Ipsum passages, and more recently with desktop publishing software like Pressmark Layout including versions of Lorem Ipsum.</p>
    <div class="more"><span>read more</span><i>›</i></div>
  </section>
  <section class="law fiscal">
    <h2>LEGISLATION FISCAL ANNOTATED</h2>
    <ul>
      <li>IRS Code - Income Tax of Individuals</li>
      <li>IRC Code - Tax Income Tax</li>
      <li>IMI Code - Property Tax</li>
      <li>RCPIT - Supplementary Rules of Procedure of the Tax Inspectorate</li>
    </ul>
  </section>
  <section class="law admin">
    <h2>ADMINISTRATIVE LAW ANNOTATED</h2>
    <ul><li>CPTA - Code of Administrative Court Procedure</li></ul>
  </section>
  <footer class="footer">
    <nav class="footer-links"><span>Home</span><span>|</span><span>Services</span><span>|</span><span>Resources</span><span>|</span><span>Partners</span><span>|</span><span>About</span><span>|</span><span>Contacts</span></nav>
    <div class="copyright">Copyright © Lexa Fiscal Community.</div>
    <div class="follow">Follow Us :</div>
    <div class="social">
      <span style="background:#2aa9e0"></span>
      <span style="background:#0b6fa8"></span>
      <span style="background:#2f4f94"></span>
      <span style="background:#c4302b"></span>
      <span style="background:#e0147f"></span>
      <span style="background:#5a6b5e"></span>
    </div>
  </footer>
</div>
</body>
</html>
```